Creative Web Design - Intl Market Research Company

We need an innovative web design for an emerging company into the international market research marketplace.

The company, Velmoran Associates, is a Trade, Investment, and Market Research company. Velmoran offers domestic and international companies increased success in the U.S. marketplace by providing a variety of services. (seen on attached brochure)

The website should be cutting edge and creative while having an easy navigation. The color is not fixed and attached logo is not finalized, feel free to post anything from conservative to progressive options. Keep in mind target customers are domestic and international businesses looking to emerge/improve in the U.S. marketplace.

Additional Company information is located in the attached documentation. The documentation is outdated & winner will have priority standing for our next projects.(logo & document re-design)
Updates

I have received a few e-mail requests and have updated the status to guaranteed payment.

Thanks!

Target Market(s)

Any company, foreign and domestic, looking to introduce their product into the U.S. marketplace.

Industry/Entity Type

Market Research

Requirements
Must have
• Easy Navigation
Should not have
• Too many buttons
Difficult navigation
Excessive Typography

```html
<!DOCTYPE html>
<html lang="en">
<head>
<meta charset="utf-8">
<title>Velmoran Associates</title>
<link href="https://fonts.googleapis.com/css2?family=Signika:wght@300;400;600&family=Open+Sans:wght@400;600&display=swap" rel="stylesheet">
<style>
:root{
  --gold:#d9c27a;
  --gold-dark:#c1a85a;
  --gold-nav-top:#cdb56a;
  --gold-nav-bottom:#b39a4c;
  --brown:#5b4a22;
  --ink:#222;
  --muted:#9a9a9a;
  --text:#555;
  --link:#1aa3d9;
  --blue:#1aa3e0;
  --navy:#2b3e6b;
  --footer:#2b2b2b;
  --footer-bottom:#3a3a3a;
  --footer-text:#c9c9c9;
}
*{box-sizing:border-box;margin:0;padding:0}
html,body{width:912px;height:1200px;overflow:hidden}
body{position:relative;background:#fff;font-family:"Open Sans",sans-serif;color:var(--ink)}
.abs{position:absolute}
.head{font-family:"Signika",sans-serif}

/* header */
.brand{left:93px;top:35px;display:flex;align-items:center;gap:10px}
.brand-mark{width:34px;height:34px;border-radius:50%;background:var(--gold-dark)}
.brand-name{font-family:"Signika",sans-serif;font-size:20px;font-weight:600;color:var(--ink)}
.order{left:664px;top:42px;font-family:"Signika",sans-serif;font-size:13px;color:var(--navy);display:flex;align-items:center;gap:8px}
.phone-num{left:672px;top:66px;font-family:"Signika",sans-serif;font-size:21px;color:var(--blue);letter-spacing:.5px}

/* nav */
.nav{left:0;top:117px;width:912px;height:35px;background:linear-gradient(var(--gold-nav-top),var(--gold-nav-bottom))}
.nav ul{list-style:none;display:flex;position:absolute;left:80px;top:0;height:35px}
.nav li{font-family:"Signika",sans-serif;font-size:12.5px;color:#fff;padding:0 20px;line-height:35px;border-left:1px solid rgba(120,95,30,.45)}
.nav li:first-child{border-left:none;color:#2a2410;padding-left:14px}
.search{left:640px;top:124px;width:188px;height:22px;background:#fff;border-radius:2px;font-size:10px;color:#aaa;padding:5px 12px}
.search svg{position:absolute;right:8px;top:4px}

/* hero */
.band{left:0;top:152px;width:912px;height:432px;background:var(--gold)}
.hero{left:84px;top:164px;width:744px;height:313px;background:linear-gradient(100deg,#e9d6cc 0%,#d9c3b4 35%,#c7b0a0 55%,#ece7e2 80%,#f3f1ef 100%)}
.finder{left:95px;top:333px;width:311px;height:134px;background:rgba(35,35,35,.88);padding:12px 13px}
.finder h2{font-family:"Signika",sans-serif;font-weight:300;font-size:25px;color:#fff}
.finder p{font-size:9.5px;color:#e5e5e5;margin-top:1px}
.finder .field{position:absolute;left:13px;top:62px;width:277px;height:26px;background:#fff;border-radius:2px;font-size:9.5px;color:#999;padding:7px 6px}
.finder .btn{position:absolute;left:13px;top:98px;width:107px;height:25px;background:#fff;font-family:"Signika",sans-serif;font-size:12.5px;text-align:center;line-height:25px}
.finder .adv{position:absolute;left:212px;top:106px;font-family:"Signika",sans-serif;font-size:10.5px;color:#fff}
.tagline{left:0;top:502px;width:912px;text-align:center;font-family:"Signika",sans-serif;font-size:21px;color:#fff;text-shadow:0 1px 3px rgba(0,0,0,.35)}
.intro{left:130px;top:536px;width:652px;text-align:center;font-size:11px;line-height:16px;color:#3b3320}

/* welcome */
.welcome{left:0;top:584px;width:912px;height:352px;background:linear-gradient(#fafafa,#ededed)}
.welcome h1{position:absolute;left:99px;top:43px;font-family:"Signika",sans-serif;font-weight:300;font-size:22px}
.welcome .copy{position:absolute;left:99px;top:77px;width:520px;font-size:9.3px;line-height:16.5px;color:var(--muted)}
.welcome .copy p+p{margin-top:5px}
.country{left:635px;top:627px;width:178px;background:#fff;box-shadow:0 1px 4px rgba(0,0,0,.25);border-radius:2px}
.country h3{background:var(--brown);color:#fff;font-family:"Signika",sans-serif;font-weight:400;font-size:13px;height:27px;line-height:29px;padding-left:13px;border-radius:2px 2px 0 0}
.country table{border-collapse:collapse;width:100%}
.country td{border:1px solid #e2e2e2;height:26px;font-size:9.5px;padding-left:17px;width:50%}
.cat{width:210px}
.cat h4{font-family:"Signika",sans-serif;font-weight:400;font-size:14px;position:relative}
.cat h4::before{content:"";position:absolute;left:-11px;top:9px;width:3px;height:3px;border-radius:50%;background:var(--ink)}
.cat p{font-size:9.5px;line-height:14.5px;color:var(--text);margin-top:4px;width:205px}
.cat a{color:var(--link);text-decoration:none}

/* footer */
.rule{left:0;top:936px;width:912px;height:3px;background:var(--gold-dark)}
.footer{left:0;top:939px;width:912px;height:217px;background:var(--footer)}
.fcol{width:156px;top:969px}
.fcol h5{font-family:"Signika",sans-serif;font-weight:400;font-size:14px;color:#fff;padding-bottom:9px;border-bottom:1px solid #555}
.fcol p{font-size:9.5px;line-height:15.5px;color:var(--footer-text);margin-top:12px}
.fcol p a{display:block;color:var(--link);text-decoration:none}
.input{width:157px;height:21px;background:#ececec;border-radius:1px;font-size:9px;color:#666;padding:4px 9px;margin-top:0}
.submit{width:62px;height:18px;background:var(--brown);color:#fff;font-size:9px;text-align:center;line-height:18px;border-radius:1px}
.social{display:flex;gap:14px;margin-top:14px;padding-left:9px}
.social span{width:22px;height:22px;border-radius:50%;background:#e8e8e8}
.bottom{left:0;top:1156px;width:912px;height:44px;background:var(--footer-bottom);font-size:9.5px;color:#ddd}
.bottom .copy{position:absolute;left:98px;top:16px}
.bottom ul{list-style:none;display:flex;gap:11px;position:absolute;right:98px;top:16px;font-family:"Signika",sans-serif;font-size:10px;color:#fff}
</style>
</head>
<body>

<header>
  <div class="abs brand"><span class="brand-mark"></span><span class="brand-name">Velmoran Associates</span></div>
  <div class="abs order">
    <svg width="15" height="15" viewBox="0 0 24 24"><path d="M6.6 10.8a15 15 0 0 0 6.6 6.6l2.2-2.2c.3-.3.7-.4 1-.2 1.1.4 2.3.6 3.6.6.6 0 1 .4 1 1V20c0 .6-.4 1-1 1A17 17 0 0 1 3 4c0-.6.4-1 1-1h3.5c.6 0 1 .4 1 1 0 1.3.2 2.5.6 3.6.1.3 0 .7-.2 1z" fill="#2b3e6b"/></svg>
    Problems ordering?
  </div>
  <div class="abs phone-num">0845 555 0192</div>
</header>

<nav class="abs nav">
  <ul><li>Home</li><li>Services</li><li>News &amp; Events</li><li>Partners</li><li>Opportunities</li><li>Contact</li></ul>
</nav>
<div class="abs search">Enter your search here
  <svg width="14" height="14" viewBox="0 0 24 24"><circle cx="10" cy="10" r="7" fill="none" stroke="#777" stroke-width="2.5"/><line x1="15" y1="15" x2="22" y2="22" stroke="#777" stroke-width="3"/></svg>
</div>

<section class="abs band"></section>
<div class="abs hero" role="img" aria-label="Photo of a smiling businesswoman in front of colleagues in a bright office"></div>
<div class="abs finder">
  <h2>Search business</h2>
  <p>Dolore eu feugiat nulla facilisis at vero eros et</p>
  <div class="field">Search Business Name.</div>
  <div class="btn">Find Out</div>
  <div class="adv">Advance Search</div>
</div>
<div class="abs tagline">Dolore eu feugiat nulla facilisis at vero eros et accumsan et iusto odio</div>
<p class="abs intro">Lorem Ipsum est simplement du faux texte employé dans la sition et la misen page avant impression. Le Lorem Ipsum est le faux texte standard de l'imprimerie depuis les années 1500.</p>

<section class="abs welcome">
  <h1>Welcome to Velmoran Associates</h1>
  <div class="copy">
    <p>Lorem Ipsum est simplement du faux texte employé dans la sition et la misen page avant impression. Le Lorem Ipsum est le faux texte standard de l'imprimerie depuis les années 1500, quand un peintre anonyme assembla ensemble des morceaux.</p>
    <p>Mais s'est aussi adapté à la bureautique informatique, sans que son contenu n'en soit modifié. Il a été popularisé dans les années 1960 grâce à la vente de feuilles Letraset contenant des passages du Lorem Ipsum, et, plus récemment, par son inclusion dans des applications de mise en page de texte,</p>
  </div>
</section>
<div class="abs country">
  <h3>Country</h3>
  <table>
    <tr><td>USA</td><td>RUSSIA</td></tr>
    <tr><td>AUSTRALIA</td><td>CHINA</td></tr>
    <tr><td>MEXICO</td><td>EAST EUROPE</td></tr>
    <tr><td>BRAZIL</td><td></td></tr>
  </table>
</div>

<div class="abs cat" style="left:121px;top:795px"><h4>Importers</h4><p>Lorem Ipsum est simplemen. See our <a>Lorem Ipsum est Page</a></p></div>
<div class="abs cat" style="left:361px;top:795px"><h4>Agents / Representatives</h4><p>Lorem Ipsum est simplemen. See our <a>Lorem Ipsum est Page</a></p></div>
<div class="abs cat" style="left:598px;top:795px"><h4>Distributors</h4><p>Lorem Ipsum est simplemen. See our <a>Lorem Ipsum est Page</a></p></div>
<div class="abs cat" style="left:121px;top:859px"><h4>Manufacturers</h4><p>Lorem Ipsum est simplemen. See our <a>Lorem Ipsum est Page</a></p></div>
<div class="abs cat" style="left:360px;top:858px"><h4>Joint Venture Partners</h4><p>Lorem Ipsum est simplemen. See our <a>Lorem Ipsum est Page</a></p></div>
<div class="abs cat" style="left:598px;top:859px"><h4>Investment Partners</h4><p>Lorem Ipsum est simplemen. See our <a>Lorem Ipsum est Page</a></p></div>

<div class="abs rule"></div>
<footer class="abs footer"></footer>

<div class="abs fcol" style="left:98px;top:968px">
  <h5>BLOGS</h5>
  <p>Dolore eu feugiat nulla facilisis at vero eros et accumsan.<a>Home (we start here)</a></p>
  <p>Dolore eu feugiat nulla facilisis at vero eros et accumsan.<a>Home (we start here)</a></p>
</div>
<div class="abs fcol" style="left:285px;top:963px">
  <h5>NEWS</h5>
  <p>Dolore eu feugiat nulla facilisis at vero eros et accumsan.</p>
  <p style="margin-top:6px">Dolore eu feugiat nulla facilisis at vero eros et accumsan.</p>
  <p style="margin-top:6px">Dolore eu feugiat nulla facilisis at vero eros et accumsan.</p>
</div>
<div class="abs fcol" style="left:476px;top:963px">
  <h5>CONTACT FORM</h5>
  <div class="input" style="margin-top:16px">Name</div>
  <div class="input" style="margin-top:9px">Email</div>
  <div class="input" style="margin-top:9px;height:39px">Address</div>
  <div class="submit" style="margin-top:11px">SUBMIT</div>
</div>
<div class="abs fcol" style="left:661px;top:963px;width:157px">
  <h5>FOLLOW US</h5>
  <div class="social"><span></span><span></span><span></span><span></span></div>
  <p style="margin-top:14px;line-height:14px">Dolore feugiat nulla facilisis at vero eroset accu msan iusto o dignissim qui blandit praesent. luptatum zzril delenit augue duis dolore te feugait nulla facilisi.</p>
</div>

<div class="abs bottom">
  <div class="copy">Copyright 2013 Velmoran Associates. All Rights Reserved.</div>
  <ul><li>Home</li><li>Services</li><li>News &amp; Events</li><li>Partners</li><li>Opportunities</li><li>Contact</li></ul>
</div>

</body>
</html>
```